Lift-Lark needs a design for a new mobile app

A new app - lift-lark.example, requires a design for its new app.

The app lets users add, create and share gym sessions. Sessions can be created, sets added and exercises chosen.

The app is currently functional on Android only (ios later), all that is required is a design for the app.

Some design assets are available (logo, colours, font), so the app should tie into these.

The design needs to be clean, simple and obvious, and all design assets will be required as part of this project.

One of the pages has % complete on the set - an icon to demonstrate this rather than a text based (eg 50%) would be great.

Screenshots will be available, along with the logos, colours and fonts.

Target Market(s)

Gym goers, all ages, male & female, fitness enthusiasts
Users of phones and tablets

Industry/Entity Type

Gym

Requirements
Must have
• Designs examples for each of the screens in the app, and an obvious selection of reusable elements (such as drop downs, radio buttons, buttons, calendar selectors, check boxes etc)
• Colours, logos and branding to fit into what is already available on the website.
• Usability and consistency are vital. Buttons should be in the same place (where possible).
• Design should help the user to complete the journey, and not get in the way.
• It should be a pleasure to use the app.
• Happy to have white space where appropriate.
• We use native elements where available.
Should not have
• Design features that waste space

```html
<!DOCTYPE html>
<html lang="en">
<head>
<meta charset="utf-8">
<title>Lift-Lark – New Session</title>
<link href="https://fonts.googleapis.com/css2?family=Roboto:wght@400;500;700&display=swap" rel="stylesheet">
<style>
  :root {
    --brand: #5b6fcf;
    --brand-dark: #5266c6;
    --ink: #212121;
    --muted: #8a8a8a;
    --line: #5a5a5a;
    --check: #2ea7e0;
    --paper: #ffffff;
    --button: #000000;
  }
  * { box-sizing: border-box; margin: 0; padding: 0; }
  html, body { width: 675px; height: 1200px; overflow: hidden; background: var(--paper); }
  body { font-family: "Roboto", Arial, sans-serif; color: var(--ink); position: relative; }

  .status-bar {
    position: absolute; left: 0; top: 0; width: 675px; height: 45px;
    background: var(--brand-dark); color: #fff;
    display: flex; align-items: center; justify-content: flex-end; gap: 8px; padding-right: 22px;
    font-size: 24px;
  }
  .status-bar svg { display: block; }

  .app-bar {
    position: absolute; left: 0; top: 45px; width: 675px; height: 105px;
    background: var(--brand); color: #fff;
  }
  .app-bar .menu { position: absolute; left: 32px; top: 38px; }
  .app-bar .title { position: absolute; left: 105px; top: 30px; font-size: 33px; font-weight: 700; line-height: 44px; }
  .app-bar .action-calendar { position: absolute; left: 532px; top: 34px; }
  .app-bar .action-info { position: absolute; left: 603px; top: 34px; }

  .field { position: absolute; border-bottom: 2px solid var(--line); }
  .field-label { display: block; font-size: 21px; color: var(--muted); line-height: 24px; }
  .field-value { display: block; font-size: 29px; line-height: 36px; margin-top: 10px; }
  .field-name { left: 30px; top: 196px; width: 615px; height: 86px; }
  .field-category { left: 30px; top: 310px; width: 291px; height: 86px; }
  .field-date { left: 356px; top: 310px; width: 289px; height: 86px; }
  .dropdown-arrow { position: absolute; right: 2px; bottom: 8px; }

  .section-title { position: absolute; left: 30px; top: 432px; font-size: 28px; line-height: 36px; }

  .exercise-list { position: absolute; left: 38px; top: 492px; list-style: none; }
  .exercise { display: flex; align-items: center; height: 73px; margin-top: -18px; margin-bottom: 18px; }
  .exercise svg { flex: none; }
  .exercise-name { margin-left: 25px; font-size: 28px; line-height: 36px; }

  .btn {
    position: absolute; left: 30px; width: 615px; height: 81px; border-radius: 7px;
    display: flex; align-items: center; justify-content: center; font-size: 25px; font-family: inherit;
  }
  .btn-save { top: 898px; background: var(--button); color: #fff; font-weight: 700; border: none; }
  .btn-cancel { top: 997px; height: 79px; background: var(--paper); color: var(--ink); font-weight: 500; border: 2px solid var(--button); }
</style>
</head>
<body>
  <div class="status-bar">
    <svg width="28" height="22" viewBox="0 0 28 22"><path d="M14 21 L0 5 A20 20 0 0 1 28 5 Z" fill="#fff"/></svg>
    <svg width="22" height="22" viewBox="0 0 22 22"><path d="M22 0 V22 H0 Z" fill="#fff"/></svg>
    <svg width="14" height="24" viewBox="0 0 14 24"><rect x="3" y="0" width="8" height="3" fill="#fff"/><rect x="0" y="3" width="14" height="21" rx="1" fill="#fff"/></svg>
    <span class="clock">12:30</span>
  </div>

  <header class="app-bar">
    <svg class="menu" width="38" height="28" viewBox="0 0 38 28"><rect y="1" width="36" height="4" fill="#fff"/><rect y="12" width="36" height="4" fill="#fff"/><rect y="23" width="36" height="4" fill="#fff"/></svg>
    <h1 class="title">New Session</h1>
    <svg class="action-calendar" width="36" height="38" viewBox="0 0 36 38">
      <rect x="3" y="6" width="30" height="30" rx="3" fill="none" stroke="#fff" stroke-width="4"/>
      <rect x="3" y="6" width="30" height="9" fill="#fff"/>
      <rect x="9" y="1" width="4" height="8" fill="#fff"/><rect x="23" y="1" width="4" height="8" fill="#fff"/>
      <rect x="19" y="21" width="8" height="8" fill="#fff"/>
    </svg>
    <svg class="action-info" width="38" height="38" viewBox="0 0 38 38">
      <circle cx="19" cy="19" r="18" fill="#fff"/>
      <rect x="17" y="16" width="4" height="13" fill="var(--brand)"/>
      <rect x="17" y="9" width="4" height="4" fill="var(--brand)"/>
    </svg>
  </header>

  <div class="field field-name">
    <span class="field-label">Session Name</span>
    <span class="field-value">My first training</span>
  </div>
  <div class="field field-category">
    <span class="field-label">Category</span>
    <span class="field-value">General</span>
    <svg class="dropdown-arrow" width="18" height="18" viewBox="0 0 18 18"><path d="M18 0 V18 H0 Z" fill="#6e6e6e"/></svg>
  </div>
  <div class="field field-date">
    <span class="field-label">Date</span>
    <span class="field-value">06 - 12 - 2007</span>
  </div>

  <h2 class="section-title">Add Exercises</h2>
  <ul class="exercise-list">
    <li class="exercise">
      <svg width="32" height="32" viewBox="0 0 32 32"><rect width="32" height="32" rx="3" fill="var(--check)"/><path d="M7 16 L13 22 L25 10" fill="none" stroke="#fff" stroke-width="4"/></svg>
      <span class="exercise-name">Battle Rope</span>
    </li>
    <li class="exercise">
      <svg width="32" height="32" viewBox="0 0 32 32"><rect x="2" y="2" width="28" height="28" rx="2" fill="none" stroke="#5a5a5a" stroke-width="4"/></svg>
      <span class="exercise-name">Kettlebell Clean and Press</span>
    </li>
    <li class="exercise">
      <svg width="32" height="32" viewBox="0 0 32 32"><rect x="2" y="2" width="28" height="28" rx="2" fill="none" stroke="#5a5a5a" stroke-width="4"/></svg>
      <span class="exercise-name">Kettlebell Lunge with Press</span>
    </li>
    <li class="exercise">
      <svg width="32" height="32" viewBox="0 0 32 32"><rect x="2" y="2" width="28" height="28" rx="2" fill="none" stroke="#5a5a5a" stroke-width="4"/></svg>
      <span class="exercise-name">Kettlebell Swings</span>
    </li>
    <li class="exercise">
      <svg width="32" height="32" viewBox="0 0 32 32"><rect width="32" height="32" rx="3" fill="var(--check)"/><path d="M7 16 L13 22 L25 10" fill="none" stroke="#fff" stroke-width="4"/></svg>
      <span class="exercise-name">Medicine Ball Slam</span>
    </li>
  </ul>

  <button class="btn btn-save" type="button">Save</button>
  <button class="btn btn-cancel" type="button">Cancel</button>
</body>
</html>
```